New design for Crewmantle

We are at the start of the process of evolving an existing business, and have just developed a new logo that will guide the look and feel of the rest of the site.

Crewmantle.com.au will be the place to go for small business owners that need guidance and tools on how to look after HR functions such as recruitment and performance management amongst other aspects.

The existing site that is going to be evolved in www.hiringcornerfolk.com.au - while some of the content will remain, the entire look of the site needs to change, and a new homepage and other pages need to be developed.

For this project, we'd like the new homepage to be designed to lead the way for how the rest of the pages will look moving forward.

We're looking for a clean, clear and modern design. It should not feel cluttered or busy

The wireframe for the new homepage, and another landing page are attached.

Target Market(s)

Small and medium business owners - slightly male skew

Industry/Entity Type

Small Business

Requirements
Must have
• - Should be clean and simple
- The overall feel from the new logo (attached to the project) should be integrated into all elements of the site
- Should communicate that the site is easy to navigate
- Should communicate that the site is friendly and approachable
- Should communicate that the site is professional (for small businesses)
Nice to have
• This homepage for this site is quite a good design reference in terms of clean design.

http://www.choremoose.com/

For Crewmantle though, the 3 boxes under the main image should appear above the fold though.

Also, happy for one other colour to be introduced to highlight call to action buttons etc.
Should not have
• Must not be cluttered
Should not introduce more than one additional colour to the existing colours from the logo

```html
<!DOCTYPE html>
<html lang="en">
<head>
<meta charset="utf-8">
<title>Crewmantle – Home</title>
<link rel="stylesheet" href="https://fonts.googleapis.com/css2?family=Open+Sans:wght@400;600;700&family=Bree+Serif&display=swap">
<style>
  :root {
    --brand-blue: #1a72c0;
    --brand-blue-dark: #1560a8;
    --nav-top: #2a8ad6;
    --nav-bottom: #1669b6;
    --side-grey: #6b6b70;
    --side-line: #8a8a8f;
    --cta-top: #86cc3c;
    --cta-bottom: #58a71c;
    --text: #3a3a3a;
    --heading: #2e2e2e;
    --panel: #eeeef0;
    --footer-top: #9a9a9e;
    --footer-bottom: #6f6f74;
    --white: #ffffff;
    --hero-top: #dcdde0;
    --hero-bottom: #c9c6c4;
  }
  * { box-sizing: border-box; margin: 0; padding: 0; }
  html, body { width: 1200px; height: 1200px; overflow: hidden; background: var(--white); }
  body { position: relative; font-family: "Open Sans", Arial, sans-serif; color: var(--text); }
  a { text-decoration: none; }

  .brand { position: absolute; left: 53px; top: 30px; display: flex; align-items: center; gap: 10px; }
  .brand-dot { width: 40px; height: 40px; border-radius: 50%; background: var(--brand-blue); }
  .brand-name { font-size: 34px; font-weight: 700; color: var(--brand-blue); letter-spacing: -0.5px; }

  .main-nav { position: absolute; left: 35px; top: 98px; width: 1129px; height: 47px;
    background: linear-gradient(var(--nav-top), var(--nav-bottom)); border-radius: 3px; display: flex; }
  .main-nav a { display: flex; align-items: center; justify-content: center; height: 100%;
    color: var(--white); font-weight: 600; font-size: 17.5px;
    border-right: 1px solid rgba(255,255,255,0.45); }
  .main-nav a:last-child { border-right: 0; }
  .nav-home { width: 88px; }
  .nav-recruit { width: 103px; }
  .nav-induction { width: 120px; }
  .nav-engage { width: 104px; }
  .nav-exit { width: 158px; }
  .nav-community { width: 139px; }
  .nav-contact { width: 90px; }

  .side-menu { position: absolute; left: 36px; top: 196px; width: 292px; height: 218px;
    background: var(--side-grey); padding-top: 34px; }
  .side-menu a { display: block; height: 35.5px; line-height: 35px; padding-left: 18px;
    color: var(--white); font-weight: 700; font-size: 17px;
    border-bottom: 1px solid var(--side-line); }
  .side-menu a:last-child { border-bottom: 0; }

  .hero-photo { position: absolute; left: 328px; top: 154px; width: 836px; height: 307px;
    border: 1px solid #55575c; border-radius: 4px;
    background: linear-gradient(180deg, var(--hero-top) 0%, #d4d2d0 55%, var(--hero-bottom) 100%); }

  .tagline { position: absolute; left: 0; top: 476px; width: 1200px; text-align: center; font-weight: 400;
    font-family: "Bree Serif", Georgia, serif; font-size: 33px; line-height: 36px; color: var(--brand-blue); }

  .cta { position: absolute; left: 426px; top: 566px; width: 327px; height: 37px;
    background: linear-gradient(var(--cta-top), var(--cta-bottom)); border: 1px solid #4f8f1f; border-radius: 2px;
    display: flex; align-items: center; justify-content: center; gap: 16px;
    font-family: "Bree Serif", Georgia, serif; font-size: 21px; color: var(--white); }

  .column { position: absolute; top: 634px; }
  .column h2 { font-size: 22px; font-weight: 600; color: var(--heading); }
  .about { left: 47px; width: 294px; }
  .about h2 { margin-bottom: 6px; }
  .text-line { display: block; text-align: justify; text-align-last: justify; white-space: nowrap; }
  .text-line.last { text-align-last: left; }
  .about p { font-size: 15px; line-height: 24.7px; }
  .about .read-more { display: block; text-align: right; margin-top: 10px; color: var(--brand-blue);
    font-weight: 600; font-size: 17px; }

  .news { left: 397px; width: 353px; top: 636px; }
  .news h2 { margin-bottom: 14px; }
  .news-item { position: relative; padding-left: 71px; margin-bottom: 36px; }
  .news-date { position: absolute; left: 0; top: -7px; width: 55px; height: 55px; border-radius: 50%;
    background: var(--brand-blue); color: var(--white); text-align: center;
    font-size: 19px; font-weight: 600; line-height: 20px; padding-top: 7px; }
  .news-item p { font-size: 15px; line-height: 21px; }
  .news-item .read-more { display: block; text-align: right; margin-top: 26px; font-size: 14px;
    font-weight: 700; color: var(--heading); }

  .partners { left: 800px; width: 364px; top: 636px; }
  .partners h2 { margin-bottom: 14px; }
  .partner-panel { width: 364px; height: 269px; background: var(--panel); border-radius: 3px; position: relative; }
  .partner-badge { position: absolute; background: var(--white); border: 1px solid #e1e1e4; }
  .badge-1 { left: 11px; top: 25px; width: 185px; height: 57px; }
  .badge-2 { left: 208px; top: 25px; width: 130px; height: 57px; }
  .badge-3 { left: 17px; top: 91px; width: 155px; height: 62px; }
  .badge-4 { left: 189px; top: 93px; width: 158px; height: 57px; }
  .badge-5 { left: 17px; top: 163px; width: 158px; height: 67px; }
  .badge-shape { position: absolute; left: 50%; top: 50%; width: 60%; height: 40%; transform: translate(-50%,-50%);
    background: #d8dbe0; border-radius: 4px; }

  .site-footer { position: absolute; left: 0; top: 970px; width: 1200px; height: 230px;
    background: linear-gradient(var(--footer-top), var(--footer-bottom)); color: var(--white); }
  .footer-col { position: absolute; top: 22px; }
  .footer-col h3 { font-size: 16px; font-weight: 400; text-transform: uppercase; margin-bottom: 6px; }
  .footer-col a, .footer-col p { display: block; font-size: 14px; font-weight: 600; line-height: 28px;
    color: var(--white); }
  .footer-col .plain { font-weight: 400; }
  .col-services { left: 47px; }
  .col-links { left: 205px; }
  .col-links a { padding-left: 2px; }
  .col-contact { left: 404px; }
  .social { position: absolute; left: 817px; width: 362px; height: 38px; background: var(--white);
    border: 1px solid #55575c; border-radius: 3px; display: flex; align-items: center; padding-left: 10px;
    color: var(--heading); font-weight: 600; font-size: 17px; }
  .social-dot { width: 30px; height: 30px; border-radius: 50%; background: var(--brand-blue-dark); margin-right: 44px; }
  .social-one { top: 25px; }
  .social-two { top: 70px; left: 819px; }
  .copyright { position: absolute; right: 32px; top: 195px; font-size: 13px; }
</style>
</head>
<body>

<header class="brand">
  <span class="brand-dot"></span>
  <span class="brand-name">Crewmantle</span>
</header>

<nav class="main-nav">
  <a class="nav-home" href="#" aria-label="Home">
    <svg width="28" height="24" viewBox="0 0 28 24" aria-hidden="true">
      <path d="M14 1 L1 12 L4.5 12 L4.5 23 L11 23 L11 16 L17 16 L17 23 L23.5 23 L23.5 12 L27 12 Z" fill="#ffffff"/>
    </svg>
  </a>
  <a class="nav-recruit" href="#">Recruit</a>
  <a class="nav-induction" href="#">Induction</a>
  <a class="nav-engage" href="#">Engage</a>
  <a class="nav-exit" href="#">Employee exit</a>
  <a class="nav-community" href="#">Community</a>
  <a class="nav-contact" href="#">Contact</a>
</nav>

<aside class="side-menu">
  <a href="#">RECRUIT</a>
  <a href="#">INDUCTION</a>
  <a href="#">ENGAGE</a>
  <a href="#">EMPLOYEE EXIT</a>
  <a href="#">COMMUNITY</a>
</aside>

<div class="hero-photo" role="img" aria-label="Photo of five smiling business professionals standing in a row"></div>

<h1 class="tagline">Australia’s leading provider of educational tools that enable a<br>successful DIY recruitment process</h1>

<a class="cta" href="#">Purchase DIY kit
  <svg width="16" height="14" viewBox="0 0 16 14" aria-hidden="true"><path d="M0 5 H8 V1 L15 7 L8 13 V9 H0 Z" fill="#ffffff"/></svg>
</a>

<section class="column about">
  <h2>About Us</h2>
  <p>
    <span class="text-line">Lorem ipsum dolor sit amet, feugiat</span>
    <span class="text-line">nostrum lobortis eam te. Fugit harum</span>
    <span class="text-line">laboramus ne sea. Mei facer recusabo</span>
    <span class="text-line">at. Ut odio menandri sadipscing sit, eu</span>
    <span class="text-line">eros dignissim cum. Et mel case dis-</span>
    <span class="text-line">sentias, qui timeam placerat accusata</span>
    <span class="text-line">ei.Lorem ipsum dolor sit amet, feugiat</span>
    <span class="text-line">nostrum lobortis eam te. Fugit harum</span>
    <span class="text-line last">laboramus ne sea.</span>
  </p>
  <a class="read-more" href="#">Read more</a>
</section>

<section class="column news">
  <h2>Latest News</h2>
  <article class="news-item">
    <div class="news-date">21<br>Jul</div>
    <p>
      <span class="text-line">Lorem ipsum dolor sit amet, feugiat</span>
      <span class="text-line">nostrum lobortis eam te. Fugit</span>
      <span class="text-line last">harum laboramus ne sea.</span>
    </p>
    <a class="read-more" href="#">Read more</a>
  </article>
  <article class="news-item">
    <div class="news-date">21<br>Jul</div>
    <p>
      <span class="text-line">Lorem ipsum dolor sit amet, feugiat</span>
      <span class="text-line">nostrum lobortis eam te. Fugit</span>
      <span class="text-line last">harum laboramus ne sea.</span>
    </p>
    <a class="read-more" href="#">Read more</a>
  </article>
</section>

<section class="column partners">
  <h2>Partners</h2>
  <div class="partner-panel">
    <div class="partner-badge badge-1"><span class="badge-shape"></span></div>
    <div class="partner-badge badge-2"><span class="badge-shape"></span></div>
    <div class="partner-badge badge-3"><span class="badge-shape"></span></div>
    <div class="partner-badge badge-4"><span class="badge-shape"></span></div>
    <div class="partner-badge badge-5"><span class="badge-shape"></span></div>
  </div>
</section>

<footer class="site-footer">
  <div class="footer-col col-services">
    <h3>Services</h3>
    <a href="#">Recruit</a>
    <a href="#">Induction</a>
    <a href="#">Engage</a>
    <a href="#">Employee exit</a>
    <a href="#">Community</a>
  </div>
  <div class="footer-col col-links">
    <h3>Other links</h3>
    <a href="#">Home</a>
    <a href="#">Sitemap</a>
    <a href="#">Privacy Policy</a>
    <a href="#">Contact Us</a>
  </div>
  <div class="footer-col col-contact">
    <h3>Contact us</h3>
    <p>Level 4, 22 Harbourline Street,</p>
    <p>SYDNEY NSW 2000</p>
    <p>&nbsp;Phone: <span class="plain">(02) 5550 1234</span></p>
    <p>&nbsp;Email: <span class="plain">info@hiringcornerfolk.com.au</span></p>
  </div>
  <a class="social social-one" href="#"><span class="social-dot"></span>Follow us on Chatterbook</a>
  <a class="social social-two" href="#"><span class="social-dot"></span>Follow us on Tweetline</a>
  <p class="copyright">Copyright 2012 Crewmantle. All rights reserved.</p>
</footer>

</body>
</html>
```